Corwith Lodge website redesign

After 8 years of our current site, we're ready to upgrade our site design. We'd like to generally make it more modern and clean and build it on a CMS like joomla for easier future maintenance.

Our hotel is a family-owned bed and breakfast that competes against much larger hotel chains in Aspen with fancier rooms and larger pricetags. Our hotel is priced moderately and features tasteful, uniquely-design rooms.

We are looking for a website that will showcase the uniqueness of our rooms, the history of the Lodge, and the friendliness of our staff.

Here are some other hotel sites we like:

http://www.brackenfoldhouse.example/

http://www.tollerpeakhaus.example/

http://www.quarrowstay.example/

*********

Scope of Work - I'm looking for a design AND build. The website should be built out in Joomla as part of the final deliverable.
Updates

Current website: http://www.corwithlodge.example/

Explanation of what design + build means:

I am looking for not only the design of the site, but also for the homepage and one subpage to be built out as well. I do NOT need the entire site built - only for those two pages to be built and I will retrofit the remainder of the pages.

Target Market(s)

travellers evaluating hotels in Aspen, Colorado.

Industry/Entity Type

Hotel

Requirements
Must have
• Must, must, must be based on a joomla template. "Rotating" large main image as central position on homepage is a must (see example websites mentioned above).

Nice to have
• We have an existing online reservation system. It would be nice to evaluate placing a "widget" on the homepage that integrates to the online reservation page. Similar to that feature that the Bracken Fold website has at the foot of the main image on their homepage.

```html
<!DOCTYPE html>
<html lang="en">
<head>
<meta charset="utf-8">
<title>Corwith Lodge</title>
<link href="https://fonts.googleapis.com/css2?family=Arimo:ital,wght@0,400;0,700;1,400&display=swap" rel="stylesheet">
<style>
  :root {
    --navy: rgba(16, 28, 48, 0.82);
    --navy-solid: #121d2f;
    --white: #ffffff;
    --page: #eef2f6;
    --panel: #ffffff;
    --side: #e4e4e4;
    --ink: #333333;
    --muted: #6b6b6b;
    --field: #f4f4f4;
    --field-border: #c9c9c9;
    --arrow: #2f3a46;
  }
  * { box-sizing: border-box; margin: 0; padding: 0; }
  html, body { width: 1200px; height: 900px; overflow: hidden; }
  body {
    position: relative;
    font-family: "Arimo", Arial, sans-serif;
    background: var(--page);
    color: var(--ink);
  }
  .hero {
    position: absolute; left: 0; top: 0; width: 1200px; height: 663px;
    background:
      linear-gradient(180deg, #2f5c9a 0%, #4a6e8e 12%, #5b3a26 30%, #6b4a35 55%, #8a7a6c 80%, #b9b1a6 100%);
  }
  .brand {
    position: absolute; left: 105px; top: 0; width: 253px; height: 100px;
    background: var(--navy); border-radius: 0 0 6px 6px;
    display: flex; align-items: center; justify-content: center;
  }
  .brand-name { color: var(--white); font-size: 30px; font-weight: 400; letter-spacing: 0.5px; }
  .topbar {
    position: absolute; left: 668px; top: 0; width: 427px; height: 31px;
    background: var(--navy); border-radius: 0 0 6px 6px;
    display: flex; align-items: center; gap: 8px; padding: 0 14px;
    color: var(--white); font-size: 11px; font-weight: 700;
  }
  .topbar .gap { width: 12px; }
  .flag { display: inline-flex; width: 12px; height: 8px; }
  .main-nav {
    position: absolute; left: 457px; top: 62px; width: 645px; height: 40px;
    background: var(--navy); border-radius: 5px;
    display: flex; align-items: center; padding: 0 8px;
  }
  .main-nav a {
    color: var(--white); text-decoration: none; font-size: 13px;
    padding: 4px 6px; margin-right: 3px;
  }
  .main-nav a.active { background: rgba(255,255,255,0.12); border-radius: 3px; }
  .slide-arrow {
    position: absolute; width: 40px; height: 40px; border-radius: 50%;
    background: rgba(20,20,20,0.85); border: 1px solid rgba(255,255,255,0.25);
  }
  .slide-arrow svg { display: block; }
  .caption {
    position: absolute; left: -6px; top: 447px; width: 853px; height: 111px;
    background: rgba(30, 30, 34, 0.62); border-radius: 0 6px 6px 0;
    border: 1px dashed rgba(255,255,255,0.35);
    padding: 16px 0 0 112px; color: var(--white);
  }
  .caption h1 { font-size: 36px; font-weight: 700; text-shadow: 0 2px 3px rgba(0,0,0,0.6); }
  .caption p { font-size: 18px; font-weight: 700; margin-top: 8px; text-shadow: 0 1px 2px rgba(0,0,0,0.6); }
  .content {
    position: absolute; left: 105px; top: 600px; width: 990px; height: 320px;
    background: var(--panel); border-radius: 6px;
    box-shadow: 0 0 6px rgba(0,0,0,0.15); overflow: hidden;
  }
  .booking {
    position: absolute; left: 0; top: 0; width: 316px; height: 100%;
    background: var(--side); border-right: 1px solid #cfcfcf; padding: 25px 41px 0 41px;
  }
  .booking h2, .column h2 { font-size: 19px; font-weight: 400; color: var(--ink); }
  .field-label { font-size: 13px; margin-top: 18px; display: block; }
  .booking .field-label:first-of-type { margin-top: 16px; }
  .field {
    margin-top: 6px; width: 232px; height: 32px; background: var(--field);
    border: 1px solid var(--field-border); border-radius: 4px;
    display: flex; align-items: center; justify-content: space-between;
    font-size: 12px; padding-left: 15px; color: var(--ink);
  }
  .field .addon {
    width: 31px; height: 100%; border-left: 1px solid var(--field-border);
    display: flex; align-items: center; justify-content: center; background: #e2e2e2;
  }
  .field-date { font-size: 13px; }
  .sep { border-top: 1px dashed #bdbdbd; margin-top: 19px; }
  .column { position: absolute; top: 25px; }
  .packages { left: 358px; width: 274px; }
  .rooms { left: 674px; width: 274px; }
  .column .lead { font-style: italic; color: var(--muted); font-size: 14px; margin-top: 5px; }
  .photo { display: block; }
  .deal-photo {
    position: relative; margin-top: 16px; width: 274px; height: 145px;
    background: radial-gradient(circle at 40% 40%, #d11a1a 0%, #a30e0e 50%, #3a0a08 100%);
  }
  .deal-caption {
    position: absolute; left: 0; bottom: 0; width: 100%; height: 48px;
    background: rgba(30,30,30,0.55); color: var(--white);
    font-weight: 700; font-size: 15px; display: flex; align-items: center; justify-content: center;
  }
  .deal-arrow {
    position: absolute; top: 104px; width: 28px; height: 28px; border-radius: 50%;
    background: var(--arrow); border: 2px solid #dfe5ea;
  }
  .deal-count { text-align: center; font-style: italic; font-size: 11px; color: var(--muted); margin-top: 22px; }
  .body-text { font-size: 13px; line-height: 19px; margin-top: 18px; }
  .room-photo {
    margin-top: 13px; width: 272px; height: 157px;
    background: linear-gradient(135deg, #6a3a1c 0%, #3a2012 40%, #9a4a3a 70%, #c9b39a 100%);
  }
  .rooms .body-text { margin-top: 11px; }
</style>
</head>
<body>
  <div class="hero" role="img" aria-label="Photo of the lodge courtyard with wooden balconies and flower boxes"></div>

  <div class="brand"><span class="brand-name">Corwith Lodge</span></div>

  <div class="topbar">
    <span>Dublin:</span>
    <svg width="15" height="15" viewBox="0 0 15 15"><circle cx="7.5" cy="7.5" r="6.5" fill="#fff"/><path d="M7.5 3.5V7.5H10.5" stroke="#121d2f" stroke-width="1.5" fill="none"/></svg>
    <span>7:10 PM</span>
    <span>&nbsp;30°C / 86° F</span>
    <svg width="18" height="14" viewBox="0 0 18 14"><circle cx="7" cy="6" r="4" fill="#f4c430"/><ellipse cx="11" cy="10" rx="6" ry="3.5" fill="#e6e6e6"/></svg>
    <span class="gap"></span>
    <span>Change language:</span>
    <svg class="flag" viewBox="0 0 12 8"><rect width="12" height="8" fill="#c60b1e"/><rect y="2" width="12" height="4" fill="#ffc400"/></svg>
    <svg class="flag" viewBox="0 0 12 8"><rect width="4" height="8" fill="#0055a4"/><rect x="4" width="4" height="8" fill="#fff"/><rect x="8" width="4" height="8" fill="#ef4135"/></svg>
    <svg class="flag" viewBox="0 0 12 8"><rect width="12" height="3" fill="#000"/><rect y="2.7" width="12" height="2.7" fill="#dd0000"/><rect y="5.3" width="12" height="2.7" fill="#ffce00"/></svg>
  </div>

  <nav class="main-nav">
    <a class="active" href="#">Home</a>
    <a href="#">Reservation</a>
    <a href="#">Rooms</a>
    <a href="#">Aspen Information</a>
    <a href="#">Location</a>
    <a href="#">Manager’s Journal</a>
    <a href="#">Amenities</a>
    <a href="#">Contact Us</a>
  </nav>

  <div class="slide-arrow" style="left:106px;top:254px;">
    <svg width="38" height="38" viewBox="0 0 38 38"><path d="M22 11L14 19L22 27" stroke="#fff" stroke-width="3" fill="none"/></svg>
  </div>
  <div class="slide-arrow" style="left:1053px;top:254px;">
    <svg width="38" height="38" viewBox="0 0 38 38"><path d="M16 11L24 19L16 27" stroke="#fff" stroke-width="3" fill="none"/></svg>
  </div>

  <div class="caption">
    <h1>Corwith Lodge: a heavenly place</h1>
    <p>With fabulous views,sky, high speed internet The Palace is the place to be!</p>
  </div>

  <main class="content">
    <section class="booking">
      <h2>Book a room online</h2>
      <span class="field-label">Type of room</span>
      <div class="field"><span>Select a type of room</span>
        <span class="addon"><svg width="10" height="6" viewBox="0 0 10 6"><path d="M0 0H10L5 6Z" fill="#444"/></svg></span>
      </div>
      <div class="sep"></div>
      <span class="field-label">Check-in date</span>
      <div class="field field-date"><span>19 / 12 / 2012</span>
        <span class="addon"><svg width="14" height="14" viewBox="0 0 14 14"><rect x="1" y="2" width="12" height="11" fill="#fff" stroke="#b33" /><rect x="1" y="2" width="12" height="3" fill="#c33"/></svg></span>
      </div>
      <div class="sep"></div>
      <span class="field-label">Check-out date</span>
      <div class="field field-date"><span>20 / 12 / 2012</span>
        <span class="addon"><svg width="14" height="14" viewBox="0 0 14 14"><rect x="1" y="2" width="12" height="11" fill="#fff" stroke="#b33" /><rect x="1" y="2" width="12" height="3" fill="#c33"/></svg></span>
      </div>
    </section>

    <section class="column packages">
      <h2>Packages &amp; Deals</h2>
      <p class="lead">We have some awesome deals!</p>
      <div class="deal-photo" role="img" aria-label="Photo of red roses">
        <div class="deal-caption">The Lovers’ week-end</div>
      </div>
      <div class="deal-arrow" style="left:-14px;">
        <svg width="24" height="24" viewBox="0 0 24 24"><path d="M14 8L10 12L14 16" stroke="#fff" stroke-width="2" fill="none"/></svg>
      </div>
      <div class="deal-arrow" style="left:259px;">
        <svg width="24" height="24" viewBox="0 0 24 24"><path d="M10 8L14 12L10 16" stroke="#fff" stroke-width="2" fill="none"/></svg>
      </div>
      <p class="deal-count">This is the Package 2 out of 5</p>
      <p class="body-text">This is a lorem ipsum for lovers. No dolor sit me</p>
    </section>

    <section class="column rooms">
      <h2>Rooms</h2>
      <p class="lead">Luxury in the heart of Aspen...</p>
      <div class="room-photo" role="img" aria-label="Photo of a guest room with a four-poster bed and lamp"></div>
      <p class="body-text">Well magna. Vivamus iaculis sagittis dapibus. Praesent nec risus arcu. Maecenas malesuada cursus mi, in iaculis sapien vehicula vel with:</p>
    </section>
  </main>
</body>
</html>
```